Tales from Kin Logo Design plus business cards design

We are a start up company that will help seniors write their memoirs...beginning with a few ancestors and their heritage and continuing through their own history...how they would like to be remembered in the next generation. I envision a card with a senior citizen at an older writing desk, writing her memoirs, with a book (maybe standing on top, leaning slightly) that has the words Tales from Kin.com on the back binding. OR maybe a senior couple walking into the sunset with the same book somewhere in the frame. Communicating the relevance of every life being significant to those that come after them...when a genealogy doesn't say enough about the details of ones life. Please note that I am open to the professionals own ideas...I am not locked into my concepts. On the back of the card I would like one or two phrases..."A Genealogy Doesn't Say Enough" and/or "Every life legacy is uniquely significant to the next generation".
Updates

I have added a couple of photos for ideas that may be used if needed.

I have both increased and committed the payment! Thanks for the reminder!

Reason: We increased the payment commitment and added some photo ideas to help.

We want to thank EVERYONE who participated in this contest. There were so many wonderful and VERY professional proposals...making it very challenging to decide on one! We are posting a new contest for a brochure now and hope many of you will participate. May God bless your endeavors.

Target Market(s)

Senior populous & baby boomer generation.

Industry/Entity Type

Business

Logo Text

Tales from Kin ordinary lives...extraordinary legacy

Requirements
Must have
• Relevant info:
Domain name: talesfromkin.com
email: info@talesfromkin.com
phone: 1-855-GAB-TALE toll free
1-717-382-5619 local
name: Doris Whitlock, M.A.
Nice to have
• photo of senior or senior couple....book with our web address on the binding. I attached two photos that could work if cropped and enhanced. Words need to be deleted from the one photo of senior at a writing desk and couple on the beach could use a sunset sky and other people cropped out. Just ideas...don't know if you have better ones or prefer a different idea.

```html
<!DOCTYPE html>
<html lang="en">
<head>
<meta charset="utf-8">
<title>Tales from Kin — Business Cards</title>
<link rel="stylesheet" href="https://fonts.googleapis.com/css2?family=Open+Sans:ital,wght@0,400;0,700;1,700&display=swap">
<style>
  :root {
    --canvas: #e4e4e6;
    --lime: #dcf870;
    --lime-deep: #cdee5a;
    --ink: #111111;
    --plum: #5b1838;
    --white: #ffffff;
    --photo-light: #b9b4ae;
    --photo-mid: #7d4a52;
    --photo-dark: #4a2a30;
  }
  * { box-sizing: border-box; margin: 0; padding: 0; }
  html, body {
    width: 1200px;
    height: 800px;
    overflow: hidden;
  }
  body {
    background: var(--canvas);
    font-family: "Open Sans", Arial, sans-serif;
    position: relative;
  }
  .card {
    position: absolute;
    top: 257px;
    width: 500px;
    height: 286px;
    border-radius: 4px;
    overflow: hidden;
    box-shadow: 0 10px 24px rgba(0,0,0,0.12), 0 2px 4px rgba(0,0,0,0.08);
  }

  /* Contact side */
  .card--contact {
    left: 60px;
    background: var(--lime);
  }
  .brand-mark {
    position: absolute;
    top: 38px;
    right: 34px;
    display: flex;
    align-items: center;
    gap: 8px;
    color: var(--ink);
    font-size: 20px;
    font-weight: 400;
  }
  .brand-mark .dot {
    width: 12px;
    height: 12px;
    border-radius: 50%;
    background: var(--ink);
  }
  .contact {
    position: absolute;
    left: 40px;
    top: 118px;
    color: var(--ink);
    font-size: 16px;
    line-height: 1.35;
  }
  .contact .name {
    font-size: 19px;
    font-weight: 700;
    margin-bottom: 2px;
  }

  /* Message side */
  .card--message {
    left: 640px;
    background: var(--lime);
  }
  .photo-area {
    position: absolute;
    inset: 0 0 auto 0;
    height: 170px;
    background:
      radial-gradient(ellipse at 70% 75%, rgba(255,255,255,0.55) 0 18%, transparent 40%),
      linear-gradient(110deg, var(--photo-light) 0%, var(--photo-mid) 45%, var(--photo-dark) 75%, var(--photo-mid) 100%);
  }
  .photo-area .brand-mark {
    top: 22px;
    left: 30px;
    right: auto;
    color: var(--white);
  }
  .photo-area .brand-mark .dot { background: var(--white); }
  .tagline-band {
    position: absolute;
    left: 0; right: 0; bottom: 0;
    height: 116px;
    background: var(--lime);
    display: flex;
    align-items: center;
    justify-content: center;
    padding: 0 40px;
  }
  .tagline {
    color: var(--plum);
    font-size: 18px;
    font-weight: 700;
    font-style: italic;
    text-align: center;
    line-height: 1.3;
  }
</style>
</head>
<body>

  <section class="card card--contact" aria-label="Business card, contact side">
    <div class="brand-mark"><span class="dot"></span><span>Tales from Kin.com</span></div>
    <div class="contact">
      <p class="name">Doris Whitlock, M.A.</p>
      <p>web: talesfromkin.com</p>
      <p>email: info@talesfromkin.com</p>
      <p>phone: 1-855-GAB-TALE toll free</p>
      <p>1-717-382-5619 local</p>
    </div>
  </section>

  <section class="card card--message" aria-label="Business card, message side">
    <div class="photo-area" role="img" aria-label="Photo of an open book resting on a red park bench">
      <div class="brand-mark"><span class="dot"></span><span>Tales from Kin.com</span></div>
    </div>
    <div class="tagline-band">
      <p class="tagline">“Every life legacy is uniquely significant to the next generation”.</p>
    </div>
  </section>

</body>
</html>
```